New Branding Logo and Stationery Design Project

We are looking for a Stationary design for a company called "Peak Rebuilders". We are a Personal Training business that helps people of diverse ages, fitness levels and goals achieve what they aspire to. We are excellent at what we do and have a high rate of results. We are highly compassionate and love helping people. We want this to show in our logo. The logo must be able to be used on websites but also allow for large printing in the future also.

On the Business Card
Front we need the logo, and underneath this the words "Your health and fitness specialists".
On the back of the card we need:
Name (this will be different on the 2 peoples cards)
Health and fitness specialist
mobile: 04XX-XXX-XXX (we will give to the winner to add)
website: www.peakrebuilders.com.au
email: info@peakrebuilders.com.au
Down the bottom of the card we need a section that says something like:
"Your next appointment date is / / time : "

On the letterhead we will need:
Logo
Peak Rebuilders Pty Ltd
Address
Phone number
Email
Website

Target Market(s)

Anyone, any age who needs help with health and fitness

Industry/Entity Type

Printing

Requirements
Must have
• Templates for business cards here:
https://www.inkmarlow.com.au/businesscards_diy.php
Should not have
• Should not be Racist, Sexist, Ageist

```html
<!DOCTYPE html>
<html lang="en">
<head>
<meta charset="utf-8">
<title>Peak Rebuilders – Business Card</title>
<link href="https://fonts.googleapis.com/css2?family=Arimo:wght@400;700&display=swap" rel="stylesheet">
<style>
  :root {
    --ink: #000000;
    --card-glow: #3b3b3b;
    --card-glow-soft: #2a2a2a;
    --brand-blue: #2a9be0;
    --icon-blue: #1f7fc4;
    --white: #ffffff;
    --page: #ffffff;
  }
  * { margin: 0; padding: 0; box-sizing: border-box; }
  html, body {
    width: 1200px;
    height: 1200px;
    overflow: hidden;
    background: var(--page);
    font-family: "Arimo", Arial, sans-serif;
  }
  .canvas { position: relative; width: 1200px; height: 1200px; }

  .card {
    position: absolute;
    left: 91px;
    width: 1018px;
    overflow: hidden;
    color: var(--white);
  }
  .card--front {
    top: 15px;
    height: 579px;
    background: radial-gradient(ellipse 55% 60% at 50% 45%, var(--card-glow) 0%, #151515 60%, var(--ink) 100%);
  }
  .card--back {
    top: 615px;
    height: 575px;
    background: radial-gradient(ellipse 45% 60% at 62% 50%, var(--card-glow-soft) 0%, #111111 65%, var(--ink) 100%);
  }

  /* Name block: plain circle + company name in one weight */
  .brand {
    position: absolute;
    display: flex;
    align-items: center;
    white-space: nowrap;
  }
  .brand__dot {
    flex: none;
    border-radius: 50%;
    background: var(--white);
  }
  .brand__name {
    font-weight: 700;
    color: var(--white);
    line-height: 1;
  }

  .card--front .brand { left: 166px; top: 188px; height: 120px; gap: 30px; }
  .card--front .brand__dot { width: 120px; height: 120px; }
  .card--front .brand__name { font-size: 64px; }

  .card--back .brand { left: 44px; top: 40px; height: 80px; gap: 20px; }
  .card--back .brand__dot { width: 80px; height: 80px; }
  .card--back .brand__name { font-size: 36px; }

  /* Front footer */
  .accent-bar {
    position: absolute;
    left: 0;
    background: var(--brand-blue);
  }
  .card--front .accent-bar { top: 533px; width: 468px; height: 34px; }
  .tagline {
    position: absolute;
    left: 482px;
    top: 532px;
    font-size: 31px;
    line-height: 36px;
    color: var(--white);
    white-space: nowrap;
  }

  /* Back details */
  .holder-name {
    position: absolute;
    left: 64px;
    top: 188px;
    font-size: 30px;
  }
  .holder-role {
    position: absolute;
    left: 64px;
    top: 230px;
    font-size: 24px;
  }
  .contact-list { position: absolute; left: 60px; top: 300px; list-style: none; }
  .contact-list li {
    display: flex;
    align-items: center;
    height: 54px;
    margin-bottom: 8px;
    font-size: 20px;
  }
  .contact-icon {
    width: 54px;
    height: 54px;
    margin-right: 10px;
    border-radius: 6px;
    background: var(--icon-blue);
    display: flex;
    align-items: center;
    justify-content: center;
  }

  .card--back .accent-bar { top: 531px; width: 412px; height: 34px; }
  .appointment {
    position: absolute;
    left: 412px;
    top: 531px;
    width: 595px;
    height: 34px;
    background: var(--white);
    color: var(--ink);
    font-size: 19px;
    line-height: 34px;
    padding-left: 10px;
    white-space: pre;
  }
</style>
</head>
<body>
<main class="canvas">

  <section class="card card--front" aria-label="Business card front">
    <div class="brand">
      <span class="brand__dot" aria-hidden="true"></span>
      <h1 class="brand__name">Peak Rebuilders</h1>
    </div>
    <div class="accent-bar"></div>
    <p class="tagline">“Your health and fitness specialists”</p>
  </section>

  <section class="card card--back" aria-label="Business card back">
    <div class="brand">
      <span class="brand__dot" aria-hidden="true"></span>
      <h2 class="brand__name">Peak Rebuilders</h2>
    </div>

    <p class="holder-name">Your Name Here</p>
    <p class="holder-role">Health and fitness specialist</p>

    <ul class="contact-list">
      <li>
        <span class="contact-icon">
          <svg width="26" height="38" viewBox="0 0 26 38" aria-hidden="true">
            <rect x="1" y="1" width="24" height="36" rx="4" fill="#ffffff"/>
            <rect x="4" y="5" width="18" height="24" fill="#1f7fc4"/>
            <circle cx="13" cy="33" r="2" fill="#1f7fc4"/>
          </svg>
        </span>
        04XX-XXX-XXX
      </li>
      <li>
        <span class="contact-icon">
          <svg width="38" height="28" viewBox="0 0 38 28" aria-hidden="true">
            <rect x="1" y="1" width="36" height="26" fill="#ffffff"/>
            <polyline points="2,2 19,16 36,2" fill="none" stroke="#1f7fc4" stroke-width="2.5"/>
          </svg>
        </span>
        info@peakrebuilders.com.au
      </li>
      <li>
        <span class="contact-icon">
          <svg width="40" height="36" viewBox="0 0 40 36" aria-hidden="true">
            <polygon points="20,2 38,18 33,18 33,34 7,34 7,18 2,18" fill="#ffffff"/>
            <rect x="16" y="22" width="8" height="12" fill="#1f7fc4"/>
          </svg>
        </span>
        www.peakrebuilders.com.au
      </li>
    </ul>

    <div class="accent-bar"></div>
    <p class="appointment">Your next appointment date is      /      /            time :</p>
  </section>

</main>
</body>
</html>
```